Business Card for Start-Up Consulting Business
TK Advisory Partners, LLC
Business Card for Start-Up Consulting Business - Consulting
Creative Brief
Professional
Roderick Lyle Pemberton
President/CEO
82 Fenwhistle Court #2410 Dover, DE 19906
info@tkapllc.example
www.tkapllc.example
On the back of the card, I would like something like: Text TKTEAM to 38217 for updates and promotions or For updates and promotions, text TKTEAM to 38217. I would also like to have our services listed on the back of the card like: We Specialize In: or Our Services Includes: *Negative Equity Financing *Tax Mitigation *Life & Health Insurance *Merchant Processing *Telecommunications *Energy Saving Programs *Marketing & Advertising and *More. And if the back is not crowded, maybe we can added the phone, fax, email and/or web address. Thanks

```html
<!DOCTYPE html>
<html lang="en">
<head>
<meta charset="utf-8">
<title>TK Advisory Partners, LLC – Business Card</title>
<link href="https://fonts.googleapis.com/css2?family=Cinzel:wght@400;600&family=Amiri&display=swap" rel="stylesheet">
<style>
  :root {
    --page-bg: #e9e7e3;
    --card-bg: #ffffff;
    --brand-blue: #1f4f91;
    --brand-green: #6db33f;
    --ink: #555a60;
    --rule: #c9ccd0;
    --icon: #3b3f44;
  }
  * { margin: 0; padding: 0; box-sizing: border-box; }
  html, body { width: 1200px; height: 914px; overflow: hidden; }
  body {
    background: var(--page-bg);
    display: flex; align-items: center; justify-content: center;
    font-family: "Cinzel", "Times New Roman", serif;
  }
  .card {
    position: relative;
    width: 1000px; height: 572px;
    background: var(--card-bg);
    box-shadow: 0 18px 40px rgba(0,0,0,0.18), 0 2px 6px rgba(0,0,0,0.12);
  }
  .brand {
    position: absolute; left: 350px; top: 92px;
    width: 560px;
  }
  .brand__blessing {
    font-family: "Amiri", serif;
    font-size: 22px; color: var(--ink);
    direction: rtl; text-align: center;
    width: 420px; margin-left: 120px;
    border-bottom: 1px solid var(--rule);
    padding-bottom: 2px;
  }
  .brand__row { display: flex; align-items: center; gap: 14px; margin-top: 8px; }
  .brand__mark {
    width: 30px; height: 30px; background: var(--brand-blue); flex: none;
  }
  .brand__name {
    font-size: 33px; font-weight: 400; color: var(--brand-blue);
    letter-spacing: 0.5px; white-space: nowrap;
  }
  .brand__tagline {
    margin-top: 4px;
    font-size: 14px; color: var(--brand-green); letter-spacing: 0.6px;
    text-align: right; width: 522px;
  }
  .person {
    position: absolute; right: 530px; top: 248px;
    text-align: right; color: var(--ink);
    font-size: 17px; line-height: 26px;
  }
  .person__name { color: var(--brand-blue); font-size: 22px; font-weight: 600; letter-spacing: 0.4px; }
  .contact {
    position: absolute; left: 510px; top: 252px;
    list-style: none; color: var(--ink);
    font-size: 16px; line-height: 25px;
  }
  .contact li { display: flex; align-items: center; gap: 10px; white-space: nowrap; }
  .contact svg { width: 15px; height: 15px; flex: none; }
  .bands { position: absolute; left: 0; top: 388px; width: 1000px; height: 80px; }
</style>
</head>
<body>
  <div class="card">
    <div class="brand">
      <p class="brand__blessing" lang="ar">بسم الله الرحمن الرحيم</p>
      <div class="brand__row">
        <span class="brand__mark"></span>
        <span class="brand__name">TK Advisory Partners, LLC</span>
      </div>
      <p class="brand__tagline">Helping Businesses Save Money</p>
    </div>

    <div class="person">
      <p class="person__name">Roderick Lyle Pemberton</p>
      <p class="person__title">President/CEO</p>
      <p>82 Fenwhistle Court #2410</p>
      <p>Dover, DE 19906</p>
    </div>

    <ul class="contact">
      <li><svg viewBox="0 0 16 16"><circle cx="8" cy="8" r="8" fill="var(--icon)"/><path d="M5 4.5l1.6-.5 1 2-1 .8a5 5 0 0 0 2.6 2.6l.8-1 2 1-.5 1.6c-3.6.2-6.7-2.9-6.5-6.5z" fill="#fff"/></svg>(302) 555-0148</li>
      <li><svg viewBox="0 0 16 16"><circle cx="8" cy="8" r="8" fill="var(--icon)"/><rect x="5.5" y="3.5" width="5" height="9" rx="1" fill="#fff"/></svg>(302) 555-0172</li>
      <li><svg viewBox="0 0 16 16"><circle cx="8" cy="8" r="8" fill="var(--icon)"/><rect x="4" y="6" width="8" height="5" fill="#fff"/><rect x="5.5" y="4" width="5" height="2" fill="#fff"/></svg>(888) 555-0136</li>
      <li><svg viewBox="0 0 16 16"><circle cx="8" cy="8" r="8" fill="var(--icon)"/><rect x="4" y="5" width="8" height="6" fill="#fff"/><path d="M4 5l4 3.5L12 5" stroke="var(--icon)" fill="none"/></svg>info@tkapllc.example</li>
      <li><svg viewBox="0 0 16 16"><circle cx="8" cy="8" r="8" fill="var(--icon)"/><circle cx="8" cy="8" r="4" fill="none" stroke="#fff"/><path d="M4 8h8M8 4v8" stroke="#fff"/></svg>www.tkapllc.example</li>
    </ul>

    <svg class="bands" viewBox="0 0 1000 80" aria-hidden="true">
      <line x1="0" y1="8" x2="1000" y2="8" stroke="var(--rule)" stroke-width="1"/>
      <polygon points="0,14 500,14 470,52 0,52" fill="var(--brand-blue)"/>
      <polygon points="508,30 1000,30 1000,64 478,64" fill="var(--brand-green)"/>
      <line x1="0" y1="58" x2="472" y2="58" stroke="var(--rule)" stroke-width="1"/>
      <line x1="510" y1="24" x2="1000" y2="24" stroke="var(--rule)" stroke-width="1"/>
    </svg>
  </div>
</body>
</html>
```